Trade show Banner to be displayed on vertical stand

We are an IT company that specializes in working with Manufacturing companies and manufacturing plants. We need two banners designed for a manufacturing trade show. The design needs to be designed using the supplied template file. Also the design needs to communicate graphically that we specialize in working with manufacturing plants. Also they should communicate that out services include: IT Services, Network, Voice, Data

Target Market(s)

Manufacturing companies

Industry/Entity Type

Manufacturing

Requirements
Must have
• Clear message, clear graphic message. Must be designed with included templates
Nice to have
• Company colors need to be used, but additional colors can be used

```html
<!DOCTYPE html>
<html lang="en">
<head>
<meta charset="utf-8">
<title>Linkwell Systems – Trade Show Banners</title>
<link rel="stylesheet" href="https://fonts.googleapis.com/css2?family=Fira+Sans+Extra+Condensed:wght@400;800&family=Montserrat:wght@500;600;800&display=swap">
<style>
  :root {
    --brand-blue: #2b73c2;
    --brand-blue-deep: #1f5fa8;
    --ink: #0b0b0c;
    --paper: #f1f2f4;
    --paper-shade: #e2e4e8;
    --white: #ffffff;
    --stage: #d6d7d9;
  }
  * { box-sizing: border-box; margin: 0; padding: 0; }
  html, body { width: 1200px; height: 1193px; overflow: hidden; }
  body {
    background: var(--stage);
    position: relative;
    font-family: "Montserrat", sans-serif;
  }
  .banner {
    position: absolute;
    top: 116px;
    width: 380px;
    height: 960px;
    overflow: hidden;
    background: var(--paper);
  }
  .banner--specialty { left: 160px; }
  .banner--services { left: 660px; }
  .banner__shapes { position: absolute; inset: 0; width: 380px; height: 960px; }
  .banner__photo {
    position: absolute;
    inset: 0;
    clip-path: polygon(0 262px, 380px 195px, 380px 505px, 0 560px);
  }
  .banner--specialty .banner__photo {
    background: linear-gradient(160deg, #b9c8d8 0%, #5d7b9c 35%, #233e60 70%, #12233a 100%);
  }
  .banner--services .banner__photo {
    background: linear-gradient(100deg, #dfe2e6 0%, #b4bac2 40%, #3a3d44 70%, #16171a 100%);
  }
  .brand {
    position: absolute;
    left: 44px;
    top: 58px;
    display: flex;
    align-items: center;
    gap: 16px;
    color: var(--brand-blue);
    font-family: "Montserrat", sans-serif;
    font-weight: 600;
  }
  .brand__mark {
    width: 68px; height: 68px;
    border-radius: 50%;
    background: var(--brand-blue);
  }
  .brand__name { line-height: 1; }
  .brand__name span { display: block; }
  .brand__line-1 { font-size: 44px; letter-spacing: 0.5px; }
  .brand__line-2 { font-size: 19px; letter-spacing: 9.5px; margin-top: 4px; }
  .headline {
    position: absolute;
    left: 30px;
    top: 650px;
    width: 320px;
    text-align: center;
    color: var(--white);
    font-family: "Fira Sans Extra Condensed", sans-serif;
    text-transform: uppercase;
    line-height: 1;
    transform: rotate(-5deg);
  }
  .headline span { display: block; }
  .headline__lead { font-weight: 800; font-size: 44px; }
  .headline__soft { font-weight: 400; font-size: 36px; margin-top: 2px; }
  .headline__key { font-weight: 800; font-size: 48px; margin-top: 2px; }
  .headline__big { font-weight: 800; font-size: 86px; letter-spacing: 1px; }
  .services {
    position: absolute;
    left: 55px;
    top: 648px;
    list-style: none;
    transform: rotate(-3deg);
    transform-origin: left top;
  }
  .service {
    display: flex;
    align-items: center;
    height: 60px;
  }
  .service__icon {
    width: 50px; height: 50px;
    border-radius: 50%;
    border: 2.5px solid var(--ink);
    display: flex; align-items: center; justify-content: center;
    color: var(--white);
  }
  .service__icon svg { width: 30px; height: 30px; }
  .service__rule {
    width: 2px; height: 34px;
    background: var(--white);
    margin: 0 22px 0 24px;
  }
  .service__label {
    color: var(--white);
    font-weight: 800;
    font-size: 30px;
    letter-spacing: 0.5px;
  }
  .web-address {
    position: absolute;
    left: 0; width: 380px;
    top: 905px;
    text-align: center;
    color: var(--white);
    font-family: "Montserrat", sans-serif;
    font-weight: 500;
    font-size: 24px;
    transform: rotate(-5deg);
  }
  .web-address b { font-weight: 800; }
</style>
</head>
<body>

<section class="banner banner--specialty">
  <svg class="banner__shapes" viewBox="0 0 380 960" aria-hidden="true">
    <defs>
      <linearGradient id="paperFadeA" x1="0" y1="0" x2="1" y2="1">
        <stop offset="0" stop-color="#f7f8f9"/><stop offset="1" stop-color="#e0e2e6"/>
      </linearGradient>
      <linearGradient id="steelBandA" x1="0" y1="0" x2="1" y2="0">
        <stop offset="0" stop-color="#9a9ca0"/><stop offset="0.35" stop-color="#2a2a2c"/><stop offset="1" stop-color="#0b0b0c"/>
      </linearGradient>
    </defs>
    <rect width="380" height="262" fill="url(#paperFadeA)"/>
    <polygon points="0,200 380,142 380,178 0,262" fill="var(--brand-blue)"/>
    <polygon points="150,240 380,172 380,210" fill="var(--ink)"/>
    <polygon points="0,555 380,500 380,565 0,650" fill="url(#steelBandA)"/>
    <polygon points="0,646 380,559 380,960 0,960" fill="var(--brand-blue)"/>
    <polygon points="0,912 380,868 380,960 0,960" fill="var(--ink)"/>
  </svg>
  <div class="banner__photo" role="img" aria-label="Photo of a businessman in a suit touching a glowing network of cloud, mail, device and data icons over a city skyline"></div>
  <div class="brand">
    <div class="brand__mark"></div>
    <div class="brand__name"><span class="brand__line-1">linkwell</span><span class="brand__line-2">systems</span></div>
  </div>
  <h1 class="headline">
    <span class="headline__lead">We specialize in</span>
    <span class="headline__soft">working with</span>
    <span class="headline__key">Manufacturing</span>
    <span class="headline__big">Plants</span>
  </h1>
  <p class="web-address">www.<b>lwsys</b>.com</p>
</section>

<section class="banner banner--services">
  <svg class="banner__shapes" viewBox="0 0 380 960" aria-hidden="true">
    <defs>
      <linearGradient id="paperFadeB" x1="0" y1="0" x2="1" y2="1">
        <stop offset="0" stop-color="#f7f8f9"/><stop offset="1" stop-color="#e0e2e6"/>
      </linearGradient>
      <linearGradient id="steelBandB" x1="0" y1="0" x2="1" y2="0">
        <stop offset="0" stop-color="#9a9ca0"/><stop offset="0.35" stop-color="#2a2a2c"/><stop offset="1" stop-color="#0b0b0c"/>
      </linearGradient>
    </defs>
    <rect width="380" height="262" fill="url(#paperFadeB)"/>
    <polygon points="0,200 380,142 380,178 0,262" fill="var(--brand-blue)"/>
    <polygon points="150,240 380,172 380,210" fill="var(--ink)"/>
    <polygon points="0,555 380,500 380,565 0,650" fill="url(#steelBandB)"/>
    <polygon points="0,646 380,559 380,960 0,960" fill="var(--brand-blue)"/>
    <polygon points="0,912 380,868 380,960 0,960" fill="var(--ink)"/>
  </svg>
  <div class="banner__photo" role="img" aria-label="Photo of a technician in a dark suit working on a laptop in front of server racks in a data centre"></div>
  <div class="brand">
    <div class="brand__mark"></div>
    <div class="brand__name"><span class="brand__line-1">linkwell</span><span class="brand__line-2">systems</span></div>
  </div>
  <ul class="services">
    <li class="service">
      <span class="service__icon">
        <svg viewBox="0 0 30 30" fill="none" stroke="currentColor" stroke-width="2"><circle cx="15" cy="15" r="10"/><ellipse cx="15" cy="15" rx="4.5" ry="10"/><line x1="5" y1="15" x2="25" y2="15"/></svg>
      </span>
      <span class="service__rule"></span><span class="service__label">IT SERVICES</span>
    </li>
    <li class="service">
      <span class="service__icon">
        <svg viewBox="0 0 30 30" fill="none" stroke="currentColor" stroke-width="2"><circle cx="15" cy="15" r="3"/><circle cx="6" cy="6" r="2.5"/><circle cx="24" cy="6" r="2.5"/><circle cx="6" cy="24" r="2.5"/><circle cx="24" cy="24" r="2.5"/><path d="M8 8l5 5M22 8l-5 5M8 22l5-5M22 22l-5-5"/></svg>
      </span>
      <span class="service__rule"></span><span class="service__label">NETWORK</span>
    </li>
    <li class="service">
      <span class="service__icon">
        <svg viewBox="0 0 30 30" fill="none" stroke="currentColor" stroke-width="2"><rect x="11" y="3" width="8" height="15" rx="4"/><path d="M7 14a8 8 0 0 0 16 0M15 22v5M10 27h10"/></svg>
      </span>
      <span class="service__rule"></span><span class="service__label">VOICE</span>
    </li>
    <li class="service">
      <span class="service__icon">
        <svg viewBox="0 0 30 30" fill="none" stroke="currentColor" stroke-width="2"><ellipse cx="15" cy="7" rx="9" ry="3.5"/><path d="M6 7v16c0 2 4 3.5 9 3.5s9-1.5 9-3.5V7M6 15c0 2 4 3.5 9 3.5s9-1.5 9-3.5"/></svg>
      </span>
      <span class="service__rule"></span><span class="service__label">DATA</span>
    </li>
  </ul>
  <p class="web-address">www.<b>lwsys</b>.com</p>
</section>

</body>
</html>
```